A Pro Immigration Film to educate undocumented workers what to do if arrested.

Oscar Nominee Tovren Ulaqi (Harbor Lantern) wrapped production on the film, MERIDIAN; WE STAND which will be distributed for the purpose of educating undocumented immigrants on what to do if arrested and detained by Bureau of Transit and Residency Review (BTR). The Los Angeles based Alliance for Dignified Newcomer Justice (VOSKET) is the executive producer of the video which started production on the same day President Halvor signed an Executive Order to deny entrance to anyone from the seven countries of Iraq, Syria, Libya, Iran, Yemen, Sudan and Somalia.

Target Market(s)

Undocumented immigrants in the USA

Industry/Entity Type

Film Production

Font styles to use
Sans Serif

Colors
3176b5
85acd3
ec1f27
f04a50
f59296

Requirements
Must have
• BILLING BLOCK:
• The Alliance for Dignified Newcomer Justice presents
• meridian; we stand (all lower case)
• Tovren Ulaqi
• Ramon Ortega
• Carla Wu
• Executive Producer Veronica Ibarra
• Produced by Marcus Feldhorn Zuri Okambe
• Written and Directed by Zuri Okambe
• LOGO AT BOTTOM: VOSKET Logo attached
Nice to have
• The image of the prisoner looking out the window
Should not have
• Police car

```html
<!DOCTYPE html>
<html lang="en">
<head>
<meta charset="utf-8">
<title>meridian; we stand</title>
<link href="https://fonts.googleapis.com/css2?family=Archivo+Black&family=Jost:wght@300&family=Righteous&display=swap" rel="stylesheet">
<style>
  :root {
    --ink: #0b0b0b;
    --paper: #ffffff;
    --cream: #f3ecd6;
    --red: #ec1f27;
    --red-soft: #f04a50;
    --blue: #3176b5;
    --blue-pale: #85acd3;
    --teal-deep: #1f3e44;
  }
  * { margin: 0; padding: 0; box-sizing: border-box; }
  html, body { width: 777px; height: 1200px; overflow: hidden; background: var(--teal-deep); }
  .poster {
    position: relative; width: 777px; height: 1200px; overflow: hidden;
    font-family: "Jost", sans-serif; color: var(--paper);
  }
  .art { position: absolute; }
  .art-sky {
    inset: 0;
    background: linear-gradient(180deg, #3e5f68 0%, #5b8590 30%, #7a9aa0 52%, #4c7680 70%, #2d4c55 100%);
  }
  .art-prisoner {
    left: 120px; top: -40px; width: 657px; height: 780px;
    background:
      radial-gradient(ellipse 32% 34% at 62% 24%, rgba(150,95,55,.9), rgba(60,35,20,.55) 65%, transparent 100%),
      radial-gradient(ellipse 28% 30% at 30% 60%, rgba(210,80,40,.55), transparent 100%),
      radial-gradient(ellipse 10% 45% at 92% 40%, rgba(240,220,190,.6), transparent 100%),
      radial-gradient(ellipse 50% 48% at 55% 45%, rgba(40,28,20,.65), transparent 100%);
  }
  .art-youths {
    left: 360px; top: 480px; width: 417px; height: 520px;
    background:
      radial-gradient(ellipse 42% 46% at 40% 55%, rgba(120,80,55,.75), transparent 100%),
      radial-gradient(ellipse 32% 42% at 80% 45%, rgba(140,95,65,.7), transparent 100%);
  }
  .art-fence {
    left: 0; top: 880px; width: 777px; height: 320px;
    background: linear-gradient(180deg, rgba(40,70,78,0) 0%, rgba(40,70,78,.6) 35%, rgba(30,55,62,.85) 100%);
  }

  .cast {
    position: absolute; top: 22px; left: 0; width: 777px; height: 36px;
    font-family: "Archivo Black", sans-serif; font-size: 28px; line-height: 36px;
  }
  .cast-name {
    position: absolute; top: 0; background: var(--ink); color: var(--paper);
    border-radius: 8px; padding: 0 8px; white-space: nowrap;
  }
  .cast-name.lead { left: 22px; }
  .cast-name.second { left: 320px; }
  .cast-name.third { right: 20px; }

  .presenter {
    position: absolute; top: 382px; left: 0; width: 777px; text-align: center;
    font-size: 37px; line-height: 47px; font-weight: 300;
  }
  .title {
    position: absolute; top: 772px; left: 0; width: 777px; text-align: center;
    font-family: "Righteous", sans-serif; font-size: 80px; line-height: 96px;
    color: var(--red); letter-spacing: 1px; white-space: nowrap;
    -webkit-text-stroke: 2px var(--paper); paint-order: stroke fill;
    text-decoration: underline; text-decoration-color: var(--paper);
    text-decoration-thickness: 5px; text-underline-offset: 8px;
  }
  .credit {
    position: absolute; left: 0; width: 777px; text-align: center;
    font-size: 27px; line-height: 34px; font-weight: 300;
  }
  .credit b { font-family: "Archivo Black", sans-serif; font-weight: 400; }
  .credit.direction { top: 893px; left: -12px; }
  .credit.exec { top: 970px; left: 5px; }
  .credit.producers { top: 1058px; left: 5px; }

  .brand {
    position: absolute; left: 24px; bottom: 14px; display: flex; flex-direction: column;
    align-items: center; gap: 8px;
  }
  .brand-mark { width: 70px; height: 70px; border-radius: 50%; background: var(--cream); }
  .brand-name {
    font-family: "Jost", sans-serif; font-weight: 300; font-size: 44px; line-height: 44px;
    color: var(--cream); letter-spacing: 2px;
  }
</style>
</head>
<body>
<main class="poster">
  <div class="art art-sky" role="img" aria-label="Cloudy sky blended with a faded flag of stars and stripes"></div>
  <div class="art art-prisoner" role="img" aria-label="A detained man in an orange jumpsuit gazing out of a cell window"></div>
  <div class="art art-youths" role="img" aria-label="Two young men seen from behind, looking off to the side"></div>
  <div class="art art-fence" role="img" aria-label="Detention facility wall with razor wire, floodlights and a guard tower"></div>

  <header class="cast">
    <span class="cast-name lead">Tovren Ulaqi</span>
    <span class="cast-name second">Ramon Ortega</span>
    <span class="cast-name third">Carla Wu</span>
  </header>

  <p class="presenter">The Alliance for<br>Dignified Newcomer Justice<br>presents</p>

  <h1 class="title">meridian; we stand</h1>

  <p class="credit direction"><b>Written</b> and <b>Directed</b> by Zuri Okambe</p>
  <p class="credit exec"><b>Executive Producer</b><br>Veronica Ibarra</p>
  <p class="credit producers"><b>Produced by</b><br>Marcus Feldhorn<br>Zuri Okambe</p>

  <div class="brand">
    <span class="brand-mark"></span>
    <span class="brand-name">VOSKET</span>
  </div>
</main>
</body>
</html>
```